Law Firm Marketing Postcard - Double Sided

6 x 11 two sided postcard. Templates attached. Two versions for back. Use either although the one with the entire bottom left blank is preferred.
Our company helps companies that are transitioning in their office space footprint, meaning they are changing where they work location -wise and/or the setup and layout. Reasons for change are generally due to - renovation, closures/expansion, acquisitions, mergers, closures, relocation or redesign. We are marketing to law firms in the NJ and Philadelphia-area.
Design we are looking for is where each side appeals differently. One side we want bold with our lime green popping against majority black background. One idea we had was maybe a page peeling or torn to reveal the green area with text. See attached as a rough visual. Certainly deviate to make it wow!
Second side - Should look more corporate to appeal to the law firm reader. We would like our service categories to be with a brief possibly with a brief description of the service or bulleted list descriptors. Up to designer to decide to or not to include description as we sometimes don't on other collateral. Required contact info and usage of the photos in some manner. This side should use our company colors but not overwhelm with the lime green.
We were also considering using, "Law Firms. Do you need to CYA..... Change Your Address?", in some way instead of the phrase - "Law Firm Plans 2024" which is on the draft attachment.

See attached files for reference materials and items to use. The Solutions Overview pdf contains alot of the info we would like included.
Pls include the text - "Consultants. Project Managers. Service Providers."
Ignore the ASSET MANAGEMENT service category that is on the Capability Statement attachment. It has been replaced with the Document Scanning etc service on the Solutions Overview pdf.
Even if rough design is provided that doesn't have every little thing listed, we can revise and tweak before final. Thanks immensely for your time!

Target Market(s)

Law Firms

Industry/Entity Type

Law

Colors
0054AA
0677BA
7BADD7
CADEEF
E8F1F8
59FF00
82FF00
B8FF75
E3FFCB
F4FFEA

Requirements
Must have
• See description
Nice to have
• See description

```html
<!DOCTYPE html>
<html lang="en">
<head>
<meta charset="utf-8">
<title>Law Firm Postcard – Front and Back</title>
<link rel="stylesheet" href="https://fonts.googleapis.com/css2?family=Anton&family=Montserrat:wght@500;600;700&family=Roboto+Condensed:wght@700&family=Titan+One&family=Open+Sans:wght@400;700&display=swap">
<style>
  :root{
    --stage:#bcbdc0;
    --black:#000;
    --lime:#7ed957;
    --lime-dark:#2a4a1c;
    --white:#fff;
    --navy:#1f2a6b;
    --red:#e3191f;
    --ink:#231f20;
    --mail:#dbe5f1;
    --photo-a:#8c96a0;
    --photo-b:#3e4a55;
  }
  *{box-sizing:border-box;margin:0;padding:0}
  html,body{width:1042px;height:1200px;overflow:hidden;background:var(--stage)}
  .card{position:absolute;left:111px;width:820px;background:var(--black);box-shadow:0 14px 12px -8px rgba(0,0,0,.28);overflow:hidden}
  .front{top:101px;height:447px}
  .back{top:623px;height:447px}
  .art{position:absolute;inset:0}

  /* front */
  .headline{position:absolute;left:30px;top:26px;font-family:"Anton",sans-serif;font-weight:400;font-size:78px;line-height:1;letter-spacing:-.5px;color:var(--white)}
  .headline .accent{color:var(--lime)}
  .year{position:absolute;left:28px;top:128px;font-family:"Titan One",sans-serif;font-size:82px;line-height:1;color:var(--white);text-shadow:4px 5px 0 var(--lime-dark)}
  .brand{position:absolute;left:324px;top:155px;display:flex;align-items:center;gap:8px;font-family:"Montserrat",sans-serif;font-weight:700;font-size:30px;color:var(--navy)}
  .brand .dot{width:18px;height:18px;border-radius:50%;background:var(--navy)}
  .services{position:absolute;top:246px;list-style:none;font-family:"Montserrat",sans-serif;font-weight:600;font-size:18px;color:var(--white)}
  .services li{height:27.3px;padding-left:15px;position:relative}
  .services li::before{content:"";position:absolute;left:0;top:4px;border-left:9px solid var(--white);border-top:7px solid transparent;border-bottom:7px solid transparent}
  .col-a{left:27px}.col-b{left:177px}
  .cta{position:absolute;left:25px;top:372px;border-left:1.5px solid var(--lime);border-top:1.5px solid var(--lime);border-top-left-radius:6px;padding:3px 0 0 8px;width:228px}
  .cta-label{font-family:"Roboto Condensed",sans-serif;font-weight:700;font-size:19px;color:var(--white);line-height:1.05}
  .cta-phone{font-family:"Roboto Condensed",sans-serif;font-weight:700;font-size:35px;color:var(--lime);line-height:1}
  .web{position:absolute;left:315px;top:403px;font-family:"Roboto Condensed",sans-serif;font-weight:700;font-size:19px;color:var(--white)}

  /* back */
  .panel{position:absolute;left:0;top:0;width:820px;height:283px;overflow:hidden}
  .pill{position:absolute;width:66px;height:93px;border-radius:33px;background:var(--lime)}
  .pill svg{position:absolute;inset:0}
  .service{position:absolute;font-family:"Montserrat",sans-serif;color:var(--white)}
  .service h3{font-weight:600;font-size:18px;line-height:1.12;color:var(--lime);margin-bottom:7px;white-space:nowrap}
  .service p{font-weight:500;font-size:10.4px;line-height:1.36}
  .notice{position:absolute;left:0;top:283px;width:528px;height:164px;background:var(--white);text-align:center;font-family:"Open Sans",sans-serif;font-weight:700;padding-top:45px}
  .notice .warn{color:var(--red);font-size:17px;line-height:1.2}
  .notice .hint{color:var(--ink);font-size:17px;margin-top:6px}
  .mailing{position:absolute;left:528px;top:283px;width:292px;height:164px;background:var(--mail);text-align:center;font-family:"Open Sans",sans-serif;font-size:18px;line-height:1.3;color:var(--ink);padding-top:44px}
</style>
</head>
<body>

<section class="card front" aria-label="Postcard front">
  <svg class="art" width="820" height="447" viewBox="0 0 820 447">
    <defs>
      <linearGradient id="frontPhoto" x1="0" y1="0" x2="1" y2="1">
        <stop offset="0" stop-color="#b9b4aa"/><stop offset=".5" stop-color="#8c96a0"/><stop offset="1" stop-color="#3e4a55"/>
      </linearGradient>
      <linearGradient id="thumbA" x1="0" y1="0" x2="0" y2="1"><stop offset="0" stop-color="#e8eef2"/><stop offset="1" stop-color="#9fb0ba"/></linearGradient>
      <linearGradient id="thumbB" x1="0" y1="0" x2="0" y2="1"><stop offset="0" stop-color="#d8c6a8"/><stop offset="1" stop-color="#a8825a"/></linearGradient>
      <linearGradient id="thumbC" x1="0" y1="0" x2="0" y2="1"><stop offset="0" stop-color="#c8ced3"/><stop offset="1" stop-color="#a08a70"/></linearGradient>
    </defs>
    <path role="img" aria-label="Photo: office chair wrapped in plastic beside moving boxes" d="M677 0 H820 V447 H683 A300 300 0 0 1 677 0 Z" fill="url(#frontPhoto)"/>
    <path d="M677 0 A300 300 0 0 0 683 447" fill="none" stroke="var(--lime)" stroke-width="7"/>
    <rect class="band" x="0" y="119" width="600" height="115" fill="var(--lime)"/>
    <circle role="img" aria-label="Photo: open-plan office interior" cx="575" cy="119" r="59" fill="url(#thumbA)" stroke="var(--lime)" stroke-width="5"/>
    <circle role="img" aria-label="Photo: shelves of paper files" cx="552" cy="230" r="59" fill="url(#thumbB)" stroke="var(--lime)" stroke-width="5"/>
    <circle role="img" aria-label="Photo: glass-walled meeting room" cx="575" cy="340" r="59" fill="url(#thumbC)" stroke="var(--lime)" stroke-width="5"/>
  </svg>
  <h1 class="headline"><span class="accent">LAW FRIM</span> PLANS</h1>
  <div class="year">2024?</div>
  <div class="brand"><span class="dot"></span>Meridane</div>
  <ul class="services col-a"><li>Relocation</li><li>Renovation</li><li>Closure</li><li>New Office</li></ul>
  <ul class="services col-b"><li>Redesign</li><li>Merger &amp; Acquisition</li><li>Hybrid &amp; Hoteling</li></ul>
  <div class="cta"><div class="cta-label">CALL NOW TODAY!</div><div class="cta-phone">555-014-2290</div></div>
  <div class="web">www.meridanews.com</div>
</section>

<section class="card back" aria-label="Postcard back">
  <div class="panel">
    <svg class="art" width="820" height="283" viewBox="0 0 820 283">
      <defs>
        <linearGradient id="backPhoto" x1="0" y1="0" x2="0" y2="1">
          <stop offset="0" stop-color="#7d858c"/><stop offset=".55" stop-color="#4c5660"/><stop offset="1" stop-color="#5b6168"/>
        </linearGradient>
      </defs>
      <path role="img" aria-label="Photo: empty office floor with columns and windows" d="M648 0 H820 V283 H697 A260 260 0 0 1 648 0 Z" fill="url(#backPhoto)"/>
      <path d="M648 0 A260 260 0 0 0 697 283" fill="none" stroke="var(--lime)" stroke-width="6"/>
    </svg>

    <div class="pill" style="left:29px;top:34px">
      <svg width="66" height="93" viewBox="0 0 66 93" fill="none" stroke="#fff" stroke-width="2">
        <rect x="14" y="22" width="38" height="50" rx="2"/>
        <rect x="29" y="30" width="7" height="7"/><rect x="29" y="43" width="7" height="7"/><rect x="29" y="56" width="7" height="7"/>
      </svg>
    </div>
    <div class="service" style="left:110px;top:30px;width:172px">
      <h3>SPACE PLANING<br>&amp; DESIGN</h3>
      <p>Planning and design to create healthy spaces according to desired function, flow, look, and feel</p>
    </div>

    <div class="pill" style="left:317px;top:34px">
      <svg width="66" height="93" viewBox="0 0 66 93" fill="none" stroke="#fff" stroke-width="2">
        <circle cx="26" cy="42" r="8"/><rect x="12" y="54" width="22" height="16"/>
        <rect x="40" y="22" width="14" height="12" rx="2"/><path d="M44 26l6 5M50 26l-6 5"/>
      </svg>
    </div>
    <div class="service" style="left:392px;top:30px;width:205px">
      <h3>DECOMMISSION</h3>
      <p>Plan, coordinate, manage, and execute all phases for decommissioning of facility, warehouse, office space, and assets (IT included - Servers, Cabling, E-waste).</p>
    </div>

    <div class="pill" style="left:29px;top:156px">
      <svg width="66" height="93" viewBox="0 0 66 93" fill="none" stroke="#fff" stroke-width="2">
        <rect x="32" y="36" width="18" height="16"/><path d="M32 44h18"/>
        <path d="M24 34v18l-6 14M24 52l6 14M24 40l8 4"/>
      </svg>
    </div>
    <div class="service" style="left:110px;top:148px;width:190px">
      <h3>MOVE<br>MANAGEMENT</h3>
      <p>Planning and Project Management of Moves/Adds/Changes, Re-stacks, and Reconfigurations with focused execution to decrease downtime and excessive costs.</p>
    </div>

    <div class="pill" style="left:317px;top:156px">
      <svg width="66" height="93" viewBox="0 0 66 93" fill="none" stroke="#fff" stroke-width="2">
        <rect x="34" y="24" width="20" height="46"/><path d="M34 38h20M44 42v8"/>
        <path d="M12 56v12h22V56M14 56h18v-6H14z"/>
      </svg>
    </div>
    <div class="service" style="left:392px;top:148px;width:205px">
      <h3>FURNITURE<br>SERVICES</h3>
      <p>Furniture procurement (purchase and leasing), delivery, receipt, dis/assembly, and installation. Surplus handling - liquidation, recycling, donation, and disposal. Refurbishment and repair</p>
    </div>
  </div>

  <div class="notice">
    <p class="warn">You MUST remove this instruction layer or it will<br>be printed.</p>
    <p class="hint">(Turn off this layer in the “Layers” pallette)</p>
  </div>
  <div class="mailing">MAILING ADDRESS AREA<br>LEFT EMPTY<br>4.0 X 2.25</div>
</section>

</body>
</html>
```